Veltrix Global Policy Document/Report Template for consistent document outputs

We need a policy document/report template that we can disseminate to staff so all produced documents look the same, and less formatting has to be done each time a policy or report is started.
VGL applies the power of biological science, physical science, and IT to solve the most challenging mission problems encompassing Forensics, Biometrics, Weapons Technical and Identity Intelligence, CBRNE, CWMD, and Public Health initiatives. Here is a list of requirements for the document:
• Cover page
o Include full logo
o Title
o Possibly a subtitle
o Version #
o Date
o We want a common look that all policy documents will follow, and it is easy to recognize
o Some color and a unique look and feel
• Header and Footer (2nd page on)
o Both header and footer must include this language: “Confidential and Proprietary - For Veltrix Global Internal Use Only,” so it appears at the top and bottom of the page
o The document title must be in either the header or footer
• Header (after first page)
o Include logo
• Footer (not counting title page)
o Must include date, and page X of Y
• 4 levels of headings, numbered 1, 1.1, 1.1.1, 1.1.1.1
• 4 levels of bullets with color/style
• Design for a callout box
• Design or a box containing a quote
• Two table designs
• Pages (other than the title page)
o Pages are primarily white
o Colors for accent and visual interest

Finally, our corporate font is Source Sans Pro.
The swirl pattern on our logo has no special meaning (but feel free to use it as a design element).

Font styles to use
Other font styles liked:
• Source Sans Pro

Requirements
Must have
• See description for more information: Cover page, header and footer, multiple heading levels, callout box, tables

```html
<!DOCTYPE html>
<html lang="en">
<head>
<meta charset="utf-8">
<title>Veltrix Global – Report Template Pages</title>
<link href="https://fonts.googleapis.com/css2?family=Source+Sans+3:ital,wght@0,400;0,600;0,700;1,700&display=swap" rel="stylesheet">
<style>
:root{
  --stage:#4a4a4a;
  --paper:#ffffff;
  --indigo:#2e2a8a;
  --indigo-deep:#1c1760;
  --ink:#2b2b2b;
  --grey-1:#b9b9b9;
  --grey-2:#dcdcdc;
  --violet:#8a3cf0;
}
*{box-sizing:border-box;margin:0;padding:0}
html,body{width:810px;height:1200px;overflow:hidden;background:var(--stage)}
body{position:relative;font-family:"Source Sans 3","Source Sans Pro",sans-serif;color:var(--ink)}
.page{position:absolute;width:121px;height:157px;background:var(--paper);overflow:hidden}
.hdr-bar{position:absolute;left:0;top:5px;width:38px;height:6px;background:var(--indigo)}
.hdr-note{position:absolute;left:39px;top:4.6px;font-size:1.75px;line-height:1.35;color:var(--indigo)}
.ftr-logo{position:absolute;left:9px;bottom:7px;font-size:2.8px;font-weight:700;color:var(--indigo);letter-spacing:.1px}
.ftr-tab{position:absolute;right:9px;bottom:7px;width:8px;height:4px;background:var(--indigo)}
.abs{position:absolute}
.h1{position:absolute;font-size:4.6px;font-weight:700;color:var(--indigo)}
.h1 span{margin-right:2.5px}
.h2{position:absolute;font-size:2.8px;font-weight:700;color:var(--indigo)}
.h2 span{margin-right:3px}
.h3{position:absolute;font-size:2.6px;font-weight:700;font-style:italic;color:var(--indigo)}
.h4{position:absolute;font-size:1.9px;font-weight:700;font-style:italic;color:var(--ink)}
.txt{position:absolute;font-size:1.75px;line-height:1.5;text-align:justify;color:var(--ink);overflow:hidden}
.cap{position:absolute;font-size:1.5px;color:#777}
.photo{position:absolute}
.ph-city{background:linear-gradient(180deg,#e6a56a 0%,#a7697a 45%,#3d3c55 100%)}
.ph-tower{background:linear-gradient(160deg,#dfe9f5 0%,#6d8fb8 45%,#1f3556 100%)}
.ph-sky{background:linear-gradient(180deg,#3f63a5 0%,#9bb6d9 50%,#2a3b5c 100%)}
.ph-lab{background:linear-gradient(90deg,#12223f 0%,#5c3a6a 40%,#c9694a 65%,#1a2b4a 100%)}
.ph-cells{background:linear-gradient(100deg,#1c1760 0%,#1b3c6e 45%,#b8455a 80%,#2a1f6b 100%)}
.ph-map{background:radial-gradient(ellipse at 50% 55%,#3b2f6b 0%,#1b1b2a 70%)}
.quote{position:absolute;border-left:.6px solid var(--indigo);padding-left:3px;font-size:2.1px;line-height:1.55;font-weight:700;color:var(--indigo)}
.quote.plain{font-weight:400;color:var(--ink);font-size:1.75px}
.tbl{position:absolute;border-collapse:collapse}
.tbl td{height:2.3px;border:.25px solid #fff;background:var(--grey-2)}
.tbl tr:nth-child(odd) td{background:var(--grey-1)}
.tbl tr:first-child td,.tbl td:first-child{background:var(--indigo)}
.toc{position:absolute;font-size:1.85px;color:var(--indigo)}
.toc li{list-style:none;display:flex;align-items:baseline;height:3.6px}
.toc li b{font-weight:700}
.toc li i{flex:1;border-bottom:.25px dotted var(--indigo);margin:0 .6px}
.toc li.sub{font-size:1.3px;height:2.2px;padding-left:2px;color:#555}
.toc-title{position:absolute;font-size:3.3px;font-weight:700;color:var(--indigo)}
.bul{position:absolute;font-size:1.75px;line-height:1.6;color:var(--ink);padding-left:2.5px}
.bul li{list-style:none;position:relative}
.bul li::before{content:"";position:absolute;left:-2px;top:.9px;width:.7px;height:.7px;border-radius:50%;background:var(--indigo)}
.cover-title{position:absolute;left:13px;top:74px;font-size:9.5px;font-weight:700;color:#111}
.cover-logo{position:absolute;right:10px;top:12px;display:flex;align-items:center;gap:1.5px;font-size:6px;font-weight:700;color:var(--indigo)}
.cover-logo i{display:block;width:4px;height:4px;border-radius:50%;background:var(--indigo)}
.meta{position:absolute;left:10px;top:17px;width:45px;font-size:1.6px;color:#fff}
.meta div{border-bottom:.25px solid rgba(255,255,255,.5);height:5px;padding-top:1.4px;padding-left:9px}
.callout{position:absolute;background:var(--indigo-deep);color:#fff;font-size:1.6px;line-height:1.45;padding:2px;text-align:justify}
</style>
</head>
<body>

<!-- Cover -->
<section class="page" style="left:101px;top:86px">
  <div class="cover-logo"><i></i>VGL</div>
  <div class="cover-title">Project</div>
</section>

<!-- Table of contents -->
<section class="page" style="left:255px;top:84px">
  <div class="hdr-bar"></div>
  <div class="hdr-note">Confidential and Proprietary - For Veltrix Global<br>International Internal Use Only.</div>
  <div class="abs" style="left:0;top:15px;width:121px;height:30px;background:var(--indigo)"></div>
  <div class="photo ph-cells" role="img" aria-label="Scientific cell imagery" style="left:60px;top:15px;width:61px;height:30px;background:linear-gradient(90deg,var(--indigo) 0%,#1b3c6e 40%,#b8455a 75%,#2a1f6b 100%)"></div>
  <div class="meta"><div>Project</div><div>Project No.</div><div>Document No.</div><div>Author</div><div>Date</div></div>
  <div class="toc-title" style="left:14px;top:52px">Table of Contents</div>
  <ul class="toc" style="left:14px;top:60px;width:93px">
    <li><b>1 Document History</b><i></i>4</li>
    <li>1.1 Revision History<i></i>4</li>
    <li>1.2 Revision History<i></i>4</li>
    <li><b>2 Conclusion</b><i></i>5</li>
    <li><b>3 Executive Summary</b><i></i>6</li>
    <li>3.1 Project Overview<i></i>6</li>
    <li>3.2 Key Achievements<i></i>6</li>
    <li><b>4 Main Report</b><i></i>7</li>
    <li>4.1 Project Objectives &amp; Scope<i></i>7</li>
    <li>4.2 Components of the Project<i></i>8</li>
    <li>4.3 Defining the Purpose<i></i>9</li>
    <li>4.4 Project Phases and Timeline<i></i>10</li>
    <li class="sub">4.4.1 Chronicle of Programs<i></i>10</li>
    <li class="sub">4.4.2 Ignimus estion<i></i>11</li>
    <li><b>4.5 Geographical Location and Site Overview</b><i></i>12</li>
    <li class="sub">4.5.1 Location Map<i></i>13</li>
  </ul>
  <div class="ftr-logo">VGL</div><div class="ftr-tab"></div>
</section>

<!-- Conclusion -->
<section class="page" style="left:440px;top:133px">
  <div class="hdr-bar"></div>
  <div class="hdr-note">Confidential and Proprietary - For Veltrix Global<br>International Internal Use Only.</div>
  <div class="h1" style="left:14px;top:16px"><span>2</span>Conclusion</div>
  <div class="quote plain" style="left:11px;top:28px;width:30px">“Vendi comnihit dunt accum hillectum exceaquam este net dolum audam fugia sitatem. Ut quas dolorio bea lum quis a volores incipit assimag nimilig endeles tisque pertiat et faceptiunt quas molorecatem nobis dentem qui blaut quo qui bea voluptatur, iuscid moluptatem. Xerore mod”</div>
  <div class="h2" style="left:14px;top:95px;font-size:2.2px">Key Takeaways</div>
  <ul class="bul" style="left:15px;top:100px;width:28px">
    <li>Et molupta tiquidic te</li><li>Evendel iducil eaquias</li><li>Soluptamento quaerna</li><li>Undi nonsequas dolo quo</li>
  </ul>
  <div class="txt" style="left:49px;top:44px;width:58px;height:100px">Vel modis sit accus, officte nturia net am inis nonse optatus doluptae dolorian voluptatur, in reped uiparum atempenum et lam quam elictatur ad minvellab invenum eaquam elia aspicil illectae venis accum ea comnit as ius as eluresttrur si rehenecae cusa volore nonsed ut adignim incient facatur. Quid mil et as modios ipsus sam susanto tem reheniti iliuptam fugiatet idenbus res voloribus volorehi enitatem quid quam veridam, voluptatur, aut hilita dolene cumque. Vendi comnihit dunt accum hillectum exceaquam este net dolum audam fugia sitatem. Ut quas dolorio bea lum quis a volores incipit assimag nimilig endeles tisque pertiat et faceptiunt quas molorecatem nobis dentem qui blaut quo qui bea voluptatur, iuscid moluptatem. Xerore modi con re con rem ipiditibus, net electot aquisci alitiberum quiae dolecust imagni iditis secearum este plabore hendell ignimus estion re omnimin conserc illabor sumquis dissus aut offici dolupid undicianis quo omnimos etur re poria cumquae pratur sequi as eicimus, odtitisit. Vendi comnihit dunt accum hillectum exceaquam este net dolum audam fugia sitatem. Ut quas dolorio bea lum quis a volores incipit assimag nimilig.</div>
  <div class="ftr-logo">VGL</div><div class="ftr-tab"></div>
</section>

<!-- Continued page -->
<section class="page" style="left:576px;top:134px">
  <div class="hdr-bar"></div>
  <div class="hdr-note">Confidential and Proprietary - For Veltrix Global<br>International Internal Use Only.</div>
  <div class="txt" style="left:14px;top:15px;width:45px;height:18px">endeles tisque pertiat et faceptiunt quas molorecatem nobis dentem qui blaut quo qui bea voluptatur,</div>
  <div class="txt" style="left:62px;top:15px;width:45px;height:18px">iuscid moluptatem. Xerore modi con re con rem ipiditibus, net electot aquisci alitiberum quiae dolecust imagni iditis secearum este plabore hendell ignimus estion re omnimin conserc illabor sumquis dissus aut.</div>
  <div class="ftr-logo">VGL</div><div class="ftr-tab"></div>
</section>

<!-- 4.6 Engineering -->
<section class="page" style="left:102px;top:257px">
  <div class="hdr-bar"></div>
  <div class="hdr-note">Confidential and Proprietary - For Veltrix Global<br>International Internal Use Only.</div>
  <div class="h2" style="left:18px;top:19px"><span>4.6</span>Engineering Approaches</div>
  <div class="txt" style="left:14px;top:25px;width:94px;height:18px">Xerore modi con re con rem ipiditibus, net electot aquisci alitiberum quiae dolecust imagni iditis secearum este plabore hendell ignimus estion re omnimin conserc illabor sumquis molorecatem nobis dentem qui blaut quo qui bea voluptatur, iuscid moluptatem. Xerore modi con re con rem ipiditibus, net electot aquisci alitiberum quiae dolecust dolorio bea lum quis a volores incipit assimag nimilig endeles tisque</div>
  <div class="photo ph-lab" role="img" aria-label="Laboratory glassware illustration" style="left:14px;top:46px;width:94px;height:24px"></div>
  <div class="txt" style="left:14px;top:71px;width:94px;height:3px">pertiat et faceptiunt quas molorecatem nobis dentem qui blaut quo qui sumquis.</div>
  <div class="quote" style="left:11px;top:89px;width:30px">“Xerore modi con re con rem ipiditibus, net electot aquisci alitiberum quiae dolecust imagni iditis secearum este plabore hendell ignimus estion re ”</div>
  <div class="txt" style="left:47px;top:90px;width:60px;height:46px">molorecatem nobis dentem qui blaut quo qui bea voluptatur, iuscid moluptatem. Xerore modi con re con rem ipiditibus, net electot aquisci alitiberum quiae dolecust dolorio bea lum quis a volores incipit assimag nimilig endeles tisque pertiat et faceptiunt quas molorecatem nobis dentem qui blaut quo qui sumquis. re omnimin conserc illabor sumquis molorecatem nobis dentem qui blaut quo qui bea voluptatur, iuscid moluptatem. Xerore modi con re con rem ipiditibus, net electot aquisci alitiberum quiae dolecust dolorio bea lum quis a volores incipit assimag nimilig</div>
  <div class="ftr-logo">VGL</div><div class="ftr-tab"></div>
</section>

<!-- Blank page -->
<section class="page" style="left:255px;top:261px">
  <div class="hdr-bar"></div>
  <div class="hdr-note">Confidential and Proprietary - For Veltrix Global<br>International Internal Use Only.</div>
  <div class="ftr-logo">VGL</div><div class="ftr-tab"></div>
</section>

<!-- Executive summary -->
<section class="page" style="left:444px;top:317px">
  <div class="hdr-bar"></div>
  <div class="hdr-note">Confidential and Proprietary - For Veltrix Global<br>International Internal Use Only.</div>
  <div class="h1" style="left:14px;top:16px"><span>3</span>Executive Summary</div>
  <div class="photo ph-tower" role="img" aria-label="Glass office towers seen from below" style="left:83px;top:15px;width:38px;height:67px"></div>
  <div class="txt" style="left:14px;top:29px;width:66px;height:20px">vendi comnihit dunt accum hillectum exceaquam este net dolum audam fugia sitatem. Ut quas dolorio bea lum quis a volores incipit assimag nimilig endeles tisque pertiat et faceptiunt quas molorecatem nobis dentem qui blaut quo qui bea voluptatur, iuscid moluptatem. Xerore modi con re con rem ipiditibus, net electot aquisci alitiberum quiae dolecust imagni iditis secearum este plabore hendell ignimus estion</div>
  <div class="h2" style="left:18px;top:56px;font-size:2.4px"><span>3.1</span>Project Overview</div>
  <div class="cap" style="left:14px;top:61px">Table 1</div>
  <table class="tbl" style="left:14px;top:64px;width:37px">
    <tr><td></td><td></td></tr><tr><td></td><td></td></tr><tr><td></td><td></td></tr><tr><td></td><td></td></tr><tr><td></td><td></td></tr>
  </table>
  <div class="h2" style="left:18px;top:92px;font-size:2.4px"><span>3.2</span>Key Achievements</div>
  <div class="txt" style="left:14px;top:98px;width:94px;height:42px">Vendi comnihit dunt accum hillectum exceaquam este net dolum audam fugia sitatem. Ut quas dolorio bea lum quis a volores incipit assimag nimilig endeles tisque pertiat et faceptiunt quas molorecatem nobis dentem qui blaut quo qui bea voluptatur, iuscid moluptatem. Xerore modi con re con rem ipiditibus, net electot aquisci alitiberum quiae dolecust imagni iditis secearum este plabore hendell ignimus estion re omnimin conserc illabor sumquis dissus aut offici dolupid undicianis quo omnimos etur re. Poria cumquae pratur sequi as eicimus, odtitisit aut officiae magnisi conse doluptatium estrum nonsed molent minti as alis asped utas nienis minimusape verum fugia. Et molupta tiquidic te evendel iducil eaquias soluptamento quaernam undi nonsequas dolo que do dolo et omnisci sita aces aces aliquiame eost occullo rererit aceat, sin nobis excest, sequo volorendi incilis asperesseque venihicit aut aut est sunt adit, que commolu ptatur autempos verumqu iandellam.</div>
  <div class="ftr-logo">VGL</div><div class="ftr-tab"></div>
</section>

<!-- Main report -->
<section class="page" style="left:581px;top:317px">
  <div class="hdr-bar"></div>
  <div class="hdr-note">Confidential and Proprietary - For Veltrix Global<br>International Internal Use Only.</div>
  <div class="h1" style="left:14px;top:16px"><span>4</span>Main Report</div>
  <div class="photo ph-sky" role="img" aria-label="Skyscrapers against a blue sky" style="left:0;top:29px;width:121px;height:48px"></div>
  <div class="h2" style="left:18px;top:82px;font-size:2.4px"><span>4.1</span>Project Objectives &amp; Scope</div>
  <div class="txt" style="left:14px;top:88px;width:45px;height:55px">Vendi comnihit dunt accum hillectum exceaquam este net dolum audam fugia sitatem. Ut quas dolorio bea lum quis a volores incipit assimag nimilig endeles tisque pertiat et faceptiunt quas molorecatem nobis dentem qui blaut quo qui bea voluptatur, iuscid moluptatem. Xerore modi con re con rem ipiditibus. Net electot aquisci alitiberum quiae dolecust imagni iditis secearum este plabore hendell ignimus estion re omnimin conserc illabor sumquis dissus aut offici dolupid undicianis quo</div>
  <div class="txt" style="left:62px;top:88px;width:45px;height:55px">omnimos etur re poria cumquae pratur sequi as eicimus, odtitisit aut officiae magnisi conse doluptatium estrum nonsed molent minti as alis asped utas nienis minimusape verum fugia. Et molupta tiquidic te evendel iducil eaquias soluptamento quaernam undi nonsequas dolo que dolo et omnisci sita aces aces aliquiame eost occullo rererit aceat, sin nobis excest, sequo volorendi incilis asperesseque venihicit aut aut est sunt adit, que commolu ptatur autempos verumqu iandellam, sincillam vellupti.</div>
  <div class="ftr-logo">VGL</div><div class="ftr-tab"></div>
</section>

<!-- 4.4.2 chart page -->
<section class="page" style="left:103px;top:426px">
  <div class="hdr-bar"></div>
  <div class="hdr-note">Confidential and Proprietary - For Veltrix Global<br>International Internal Use Only.</div>
  <div class="h3" style="left:71px;top:14px">4.4.2 &nbsp;&nbsp; Ignimus<br>&nbsp;&nbsp;&nbsp;&nbsp;&nbsp;&nbsp;&nbsp;&nbsp;&nbsp;&nbsp;estion</div>
  <svg class="abs" style="left:14px;top:24px" width="93" height="49" viewBox="0 0 93 49">
    <rect x=".2" y=".2" width="92.6" height="48.6" fill="#fff" stroke="#ddd" stroke-width=".3"/>
    <text x="46.5" y="4.5" font-size="2.4" fill="#777" text-anchor="middle" font-family="Source Sans 3,sans-serif">Sales</text>
    <g stroke="#eee" stroke-width=".25"><line x1="5" y1="8" x2="89" y2="8"/><line x1="5" y1="15" x2="89" y2="15"/><line x1="5" y1="22" x2="89" y2="22"/><line x1="5" y1="29" x2="89" y2="29"/><line x1="5" y1="36" x2="89" y2="36"/><line x1="5" y1="42" x2="89" y2="42"/></g>
    <polyline points="5,10 31,29 57,35 85,36" fill="none" stroke="var(--indigo)" stroke-width=".7"/>
    <line x1="41" y1="46.5" x2="45" y2="46.5" stroke="var(--indigo)" stroke-width=".6"/>
    <text x="46" y="47" font-size="1.3" fill="#777" font-family="Source Sans 3,sans-serif">Sales</text>
  </svg>
  <div class="cap" style="left:14px;top:75px">Figure 3</div>
  <div class="txt" style="left:14px;top:79px;width:94px;height:26px">molorecatem nobis dentem qui blaut quo qui bea voluptatur, iuscid moluptatem. Xerore modi con re con rem ipiditibus, net electot aquisci alitiberum quiae dolecust dolorio bea lum quis a volores incipit assimag nimilig endeles tisque pertiat et faceptiunt quas molorecatem nobis dentem qui blaut quo qui bea voluptatur, iuscid moluptatem. Xerore modi con re con rem ipiditibus, net electot aquisci alitiberum quiae dolecust imagni iditis secearum este plabore hendell ignimus estion re omnimin conserc.</div>
  <div class="h4" style="left:28px;top:106px">4.4.2.1 &nbsp;&nbsp; Illabor sumquis</div>
  <div class="txt" style="left:14px;top:109px;width:94px;height:14px">dolorio bea lum quis a volores incipit assimag nimilig endeles tisque pertiat et faceptiunt quas molorecatem nobis dentem qui blaut quo qui bea voluptatur, iuscid moluptatem. Xerore modi con re con rem ipiditibus, net electot aquisci alitiberum quiae dolecust imagni iditis secearum este plabore hendell</div>
  <div class="h4" style="left:28px;top:125px">4.4.2.2 &nbsp;&nbsp; Dolorio bea</div>
  <div class="txt" style="left:14px;top:128px;width:94px;height:10px">Ium quis a volores incipit assimag nimilig endeles tisque pertiat et faceptiunt quas molorecatem nobis dentem qui blaut quo qui bea voluptatur, iuscid moluptatem. Xerore modi con re con rem ipiditibus, net electot aquisci alitiberum quiae dolecust</div>
  <div class="ftr-logo">VGL</div><div class="ftr-tab"></div>
</section>

<!-- 4.4.2.3 text page -->
<section class="page" style="left:260px;top:426px">
  <div class="hdr-bar"></div>
  <div class="hdr-note">Confidential and Proprietary - For Veltrix Global<br>International Internal Use Only.</div>
  <div class="txt" style="left:14px;top:14px;width:94px;height:5px">imagni iditis secearum este plabore hendell ignimus estion re omnimin conserc illabor sumquis</div>
  <div class="h4" style="left:28px;top:22px">4.4.2.3 &nbsp;&nbsp; Poria cumquae pratur</div>
  <div class="txt" style="left:14px;top:25px;width:94px;height:30px">sequi as eicimus, odtitisit aut officiae magnisi conse doluptatium estrum nonsed molent minti as alis asped utas nienis minimusape verum fuga. Et molupta tiquidic te evendel iducil eaquias soluptamento quaernam undi nonsequas dolo que dolo et omnisci sita aces aces aliquiame eost occullo rererit aceat, sin nobis excest, sequo volorendi incilis asperesseque venihicit aut aut est sunt adit, que commolu ptatur autempos verumqu iandellam, sincillam vellupti optatur? Equatur maxim dolorem nusdanimin poria quaturendisi si anda qui odis vel modis sit accus, officte nturia net am inis nonse</div>
  <div class="h4" style="left:28px;top:58px">4.4.2.4 &nbsp;&nbsp; Poria cumquae pratur sequi as</div>
  <div class="txt" style="left:14px;top:61px;width:94px;height:30px">eicimus, odtitisit aut officiae magnisi conse doluptatium estrum nonsed molent minti as alis asped utas nienis minimusape verum fugia. Et molupta tiquidic te evendel iducil eaquias soluptamento quaernam undi nonsequas dolo que dolo et omnisci sita aces aces aliquiame eost occullo rererit aceat, sin nobis excest, sequo volorendi incilis asperesseque venihicit aut aut est sunt adit, que commolu ptatur autempos verumqu iandellam, sincillam vellupti optatur? Equatur maxim dolorem nusdanimin poria quaturendisi si anda qui odis vel modis sit accus, officte nturia net am inis nonse</div>
  <div class="h4" style="left:28px;top:94px">4.4.2.5 &nbsp;&nbsp; Quaernam undi</div>
  <div class="txt" style="left:14px;top:97px;width:94px;height:14px">nonsequas dolo que dolo et omnisci sita aces aces aliquiame eost occullo rererit aceat, sin nobis excest, sequo volorendi incilis asperesseque venihicit aut aut est sunt adit, que commolu ptatur autempos verumqu iandellam, sincillam vellupti optatur? Equatur maxim dolorem nusdanimin poria.</div>
  <div class="h4" style="left:28px;top:114px">4.4.2.6 &nbsp;&nbsp; Quaernam</div>
  <div class="txt" style="left:14px;top:117px;width:94px;height:20px">undi nonsequas dolo que dolo et omnisci sita aces aces aliquiame eost occullo rererit aceat, sin nobis excest, sequo volorendi incilis asperesseque venihicit aut aut est sunt adit, que commolu ptatur autempos verumqu iandellam, sincillam vellupti optatur? Equatur maxim dolorem nusdanimin poria quaturendisi si anda qui odis vel modis sit accus, officte nturia net am inis nonse</div>
  <div class="ftr-logo">VGL</div><div class="ftr-tab"></div>
</section>

<!-- References -->
<section class="page" style="left:448px;top:492px">
  <div class="hdr-bar"></div>
  <div class="hdr-note">Confidential and Proprietary - For Veltrix Global<br>International Internal Use Only.</div>
  <div class="h1" style="left:14px;top:16px"><span>5</span>References</div>
  <div class="ftr-logo">VGL</div><div class="ftr-tab"></div>
</section>

<!-- Appendices -->
<section class="page" style="left:581px;top:492px">
  <div class="hdr-bar"></div>
  <div class="hdr-note">Confidential and Proprietary - For Veltrix Global<br>International Internal Use Only.</div>
  <div class="h1" style="left:14px;top:16px"><span>6</span>Appendices</div>
  <div class="h2" style="left:18px;top:29px;font-size:2.4px"><span>6.1</span>Appendices 1</div>
  <div class="h2" style="left:18px;top:41px;font-size:2.4px"><span>6.2</span>Appendices 2</div>
  <div class="ftr-logo">VGL</div><div class="ftr-tab"></div>
</section>

<!-- 4.5 Geographical -->
<section class="page" style="left:106px;top:600px">
  <div class="hdr-bar"></div>
  <div class="hdr-note">Confidential and Proprietary - For Veltrix Global<br>International Internal Use Only.</div>
  <div class="h2" style="left:18px;top:16px"><span>4.5</span>Geographical Location and Site Overview</div>
  <div class="photo ph-city" role="img" aria-label="City skyline at sunset" style="left:14px;top:25px;width:94px;height:38px"></div>
  <div class="callout" style="left:21px;top:41px;width:34px;height:43px">dolorio bea lum quis a volores incipit assimag nimilig endeles tisque pertiat et faceptiunt quas molorecatem nobis dentem qui blaut quo qui bea voluptatur, iuscid moluptatem. Xerore modi con re con rem ipiditibus, net electot aquisci alitiberum quiae dolecust imagni iditis secearum este plabore hendell ignimus estion re</div>
  <div class="h2" style="left:67px;top:64px;font-size:2px">Key Achievements</div>
  <ul class="bul" style="left:70px;top:68px;width:36px">
    <li>aquisci alitiberum quiae dolecust</li><li>imagni iditis secearum este plabore</li><li>aquisci alitiberum quiae</li>
  </ul>
  <div class="txt" style="left:14px;top:92px;width:94px;height:48px">molorecatem nobis dentem qui blaut quo qui bea voluptatur, iuscid moluptatem. Xerore modi con re con rem ipiditibus, net electot aquisci alitiberum quiae dolecust dolorio bea lum quis a volores incipit assimag nimilig endeles tisque pertiat et faceptiunt quas molorecatem nobis dentem qui blaut quo qui bea voluptatur, iuscid moluptatem. Xerore modi con re con rem ipiditibus, net electot aquisci alitiberum quiae dolecust imagni iditis secearum este plabore hendell ignimus estion re omnimin conserc illabor sumquis molorecatem nobis dentem qui blaut quo qui bea voluptatur, iuscid moluptatem. Xerore modi con re con rem ipiditibus, net electot aquisci alitiberum quiae dolecust dolorio bea lum quis a volores incipit assimag nimilig endeles tisque pertiat et faceptiunt quas molorecatem nobis dentem qui blaut quo qui sumquis.</div>
  <div class="ftr-logo">VGL</div><div class="ftr-tab"></div>
</section>

<!-- 4.5.1 Location map -->
<section class="page" style="left:261px;top:601px">
  <div class="hdr-bar"></div>
  <div class="hdr-note">Confidential and Proprietary - For Veltrix Global<br>International Internal Use Only.</div>
  <div class="h3" style="left:22px;top:14px">4.5.1 &nbsp;&nbsp; Location Map</div>
  <div class="photo ph-map" role="img" aria-label="World map with dotted continents" style="left:14px;top:19px;width:94px;height:39px"></div>
  <div class="txt" style="left:14px;top:62px;width:94px;height:22px">molorecatem nobis dentem qui blaut quo qui bea voluptatur, iuscid moluptatem. Xerore modi con re con rem ipiditibus, net electot aquisci alitiberum quiae dolecust dolorio bea lum quis a volores incipit assimag nimilig endeles tisque pertiat et faceptiunt quas molorecatem nobis dentem qui blaut quo qui bea voluptatur, iuscid moluptatem. Xerore modi con re con rem ipiditibus.</div>
  <svg class="abs" style="left:14px;top:87px" width="93" height="42" viewBox="0 0 93 42">
    <rect x=".2" y=".2" width="92.6" height="41.6" fill="#fff" stroke="#ddd" stroke-width=".3"/>
    <text x="46.5" y="4" font-size="2.2" fill="#777" text-anchor="middle" font-family="Source Sans 3,sans-serif">Series 1</text>
    <g fill="var(--indigo)">
      <rect x="11" y="11" width="8" height="25"/><rect x="32" y="22" width="8" height="14"/><rect x="53" y="16" width="8" height="20"/><rect x="74" y="10" width="8" height="26"/>
    </g>
    <line x1="5" y1="36" x2="89" y2="36" stroke="#ccc" stroke-width=".25"/>
    <circle cx="42.5" cy="39.5" r=".5" fill="var(--indigo)"/>
    <text x="43.5" y="40" font-size="1.2" fill="#777" font-family="Source Sans 3,sans-serif">Series 1</text>
  </svg>
  <div class="cap" style="left:14px;top:131px">Figure 4</div>
  <div class="ftr-logo">VGL</div><div class="ftr-tab"></div>
</section>

<!-- Table of contents continued -->
<section class="page" style="left:448px;top:679px">
  <div class="hdr-bar"></div>
  <div class="hdr-note">Confidential and Proprietary - For Veltrix Global<br>International Internal Use Only.</div>
  <ul class="toc" style="left:14px;top:14px;width:93px">
    <li><b>4.6 Engineering Approaches</b><i></i>14</li>
    <li><b>5 References</b><i></i>15</li>
    <li><b>6 Appendices</b><i></i>16</li>
    <li><b>6.1 Appendices 1</b><i></i>16</li>
    <li><b>6.2 Appendices 2</b><i></i>16</li>
  </ul>
  <div class="toc-title" style="left:14px;top:51px">Tables</div>
  <ul class="toc" style="left:14px;top:59px;width:93px;color:#555">
    <li>Table 1<i></i>4</li><li>Table 2<i></i>4</li><li>Table 3<i></i>6</li>
  </ul>
  <div class="toc-title" style="left:14px;top:77px">Figures</div>
  <ul class="toc" style="left:14px;top:85px;width:93px;color:#555">
    <li>Figure 1<i></i>8</li><li>Figure 2<i></i>10</li><li>Figure 3<i></i>11</li><li>Figure 4<i></i>13</li>
  </ul>
  <div class="ftr-logo">VGL</div><div class="ftr-tab"></div>
</section>

<!-- Document history -->
<section class="page" style="left:584px;top:677px">
  <div class="hdr-bar"></div>
  <div class="hdr-note">Confidential and Proprietary - For Veltrix Global<br>International Internal Use Only.</div>
  <div class="h1" style="left:14px;top:16px"><span>1</span>Document History</div>
  <div class="h2" style="left:18px;top:28px;font-size:2.4px"><span>1.1</span>Revision History</div>
  <div class="txt" style="left:14px;top:34px;width:94px;height:3px">The document has been revised by:</div>
  <div class="cap" style="left:14px;top:40px">Table 1</div>
  <table class="tbl" style="left:14px;top:44px;width:93px">
    <tr><td></td><td></td><td></td><td></td><td></td></tr><tr><td></td><td></td><td></td><td></td><td></td></tr><tr><td></td><td></td><td></td><td></td><td></td></tr><tr><td></td><td></td><td></td><td></td><td></td></tr><tr><td></td><td></td><td></td><td></td><td></td></tr>
  </table>
  <div class="h2" style="left:18px;top:69px;font-size:2.4px"><span>1.2</span>Revision History</div>
  <div class="txt" style="left:14px;top:75px;width:94px;height:3px">Please see the following documents for more information:</div>
  <div class="cap" style="left:14px;top:80px">Table 2</div>
  <table class="tbl" style="left:14px;top:84px;width:93px">
    <tr><td></td><td></td><td></td><td></td><td></td></tr><tr><td></td><td></td><td></td><td></td><td></td></tr><tr><td></td><td></td><td></td><td></td><td></td></tr><tr><td></td><td></td><td></td><td></td><td></td></tr><tr><td></td><td></td><td></td><td></td><td></td></tr>
  </table>
  <div class="ftr-logo">VGL</div><div class="ftr-tab"></div>
</section>

<!-- 4.2 Components -->
<section class="page" style="left:104px;top:788px">
  <div class="hdr-bar"></div>
  <div class="hdr-note">Confidential and Proprietary - For Veltrix Global<br>International Internal Use Only.</div>
  <div class="txt" style="left:14px;top:15px;width:45px;height:5px">optatur? Equatur maxim dolorem</div>
  <div class="txt" style="left:62px;top:15px;width:45px;height:5px">nusdanimin poria quaturendisi si anda qui odis vel modis</div>
  <div class="h2" style="left:18px;top:24px"><span>4.2</span>Components of the Project</div>
  <div class="txt" style="left:14px;top:30px;width:94px;height:12px">Vendi comnihit dunt accum hillectum exceaquam este net dolum audam fugia sitatem. Ut quas dolorio bea lum quis a volores incipit assimag nimilig endeles tisque pertiat et faceptiunt quas molorecatem nobis dentem qui blaut quo qui bea voluptatur, iuscid moluptatem. Xerore modi con re con rem ipiditibus,</div>
  <svg class="abs" style="left:14px;top:43px" width="86" height="51" viewBox="0 0 86 51">
    <rect x=".2" y=".2" width="85.6" height="50.6" fill="#fff" stroke="#e3e3e3" stroke-width=".3"/>
    <text x="43" y="4" font-size="2.2" fill="#777" text-anchor="middle" font-family="Source Sans 3,sans-serif">Sales</text>
    <g transform="translate(43,25)">
      <path d="M0,0 L0,-18 A18,18 0 1,1 -11.6,13.8 Z" fill="#140f5e"/>
      <path d="M0,0 L-11.6,13.8 A18,18 0 0,1 -17.1,-5.6 Z" fill="var(--violet)"/>
      <path d="M0,0 L-17.1,-5.6 A18,18 0 0,1 -10,-15 Z" fill="#6a5cf0"/>
      <path d="M0,0 L-10,-15 A18,18 0 0,1 0,-18 Z" fill="#3a34a8"/>
    </g>
    <g font-size="1.1" fill="#777" font-family="Source Sans 3,sans-serif">
      <circle cx="28" cy="48" r=".5" fill="#140f5e"/><text x="29" y="48.4">1st Qtr</text>
      <circle cx="36" cy="48" r=".5" fill="var(--violet)"/><text x="37" y="48.4">2nd Qtr</text>
      <circle cx="44" cy="48" r=".5" fill="#6a5cf0"/><text x="45" y="48.4">3rd Qtr</text>
      <circle cx="52" cy="48" r=".5" fill="#3a34a8"/><text x="53" y="48.4">4th Qtr</text>
    </g>
  </svg>
  <div class="cap" style="left:14px;top:96px">Figure 1</div>
  <div class="txt" style="left:14px;top:107px;width:45px;height:33px">Vendi comnihit dunt accum hillectum exceaquam este net dolum audam fugia sitatem. Ut quas dolorio bea lum quis a volores incipit assimag nimilig endeles tisque pertiat et faceptiunt quas molorecatem nobis dentem qui blaut quo qui bea voluptatur, iuscid moluptatem. Xerore modi con re con rem ipiditibus,</div>
  <div class="txt" style="left:62px;top:107px;width:45px;height:33px">Vendi comnihit dunt accum hillectum exceaquam este net dolum audam fugia sitatem. Ut quas dolorio bea lum quis a volores incipit assimag nimilig endeles tisque pertiat et faceptiunt quas molorecatem nobis dentem qui blaut quo qui bea voluptatur, iuscid moluptatem. Xerore modi con re con rem ipiditibus,</div>
  <div class="ftr-logo">VGL</div><div class="ftr-tab"></div>
</section>

<!-- 4.3 Defining the purpose -->
<section class="page" style="left:261px;top:789px">
  <div class="hdr-bar"></div>
  <div class="hdr-note">Confidential and Proprietary - For Veltrix Global<br>International Internal Use Only.</div>
  <div class="txt" style="left:14px;top:15px;width:45px;height:16px">Vendi comnihit dunt accum hillectum exceaquam este net dolum audam fugia sitatem. Ut quas dolorio bea lum quis a volores incipit assimag nimilig endeles tisque pertiat et faceptiunt</div>
  <div class="txt" style="left:62px;top:15px;width:45px;height:16px">quas molorecatem nobis dentem qui blaut quo qui bea voluptatur, iuscid moluptatem. Xerore modi con re con rem ipiditibus,</div>
  <div class="h2" style="left:18px;top:35px"><span>4.3</span>Defining the Purpose</div>
  <div class="photo ph-tower" role="img" aria-label="Tall glass office tower" style="left:15px;top:42px;width:45px;height:74px"></div>
  <div class="txt" style="left:63px;top:42px;width:44px;height:75px">rem ipiditibus, net electot aquisci alitiberum quiae dolecust imagni iditis secearum este plabore hendell ignimus estion re omnimin conserc illabor sumquis dissus aut offici dolupid undicianis quo omnimos etur re poria cumquae pratur sequi as eicimus, odtitisit aut officiae magnisi conse doluptatium estrum nonsed molent minti as alis asped utas nienis minimusape verum fuga. Et molupta tiquidic te evendel iducil eaquias soluptamento. Xerore modi con re con rem ipiditibus, net electot aquisci alitiberum quiae dolecust imagni iditis secearum este plabore hendell ignimus estion re omnimin conserc illabor sumquis dissus aut offici dolupid undicianis quo omnimos etur re poria cumquae pratur sequi as eicimus, odtitisit aut officiae magnisi conse magnisi conse doluptatium estrum nonsed molent minti as alis asped utas nienis minimusape verum fuga. Et molupta tiquidic te evendel iducil eaquias soluptamento.</div>
  <div class="photo ph-sky" role="img" aria-label="Modern glass buildings" style="left:15px;top:127px;width:93px;height:30px"></div>
  <div class="ftr-tab"></div>
</section>

<!-- 4.4 Phases and timeline -->
<section class="page" style="left:104px;top:961px">
  <div class="photo ph-sky" role="img" aria-label="Edge of a building photograph" style="left:14px;top:0;width:93px;height:3px"></div>
  <div class="hdr-bar"></div>
  <div class="hdr-note">Confidential and Proprietary - For Veltrix Global<br>International Internal Use Only.</div>
  <div class="h2" style="left:18px;top:16px"><span>4.4</span>Project Phases and Timeline</div>
  <div class="txt" style="left:14px;top:22px;width:94px;height:21px">Vendi comnihit dunt accum hillectum exceaquam este net dolum audam fugia sitatem. Ut quas dolorio bea lum quis a volores incipit assimag nimilig endeles tisque pertiat et faceptiunt quas molorecatem nobis dentem qui blaut quo qui bea voluptatur, iuscid moluptatem. Xerore modi con re con rem ipiditibus, net electot aquisci alitiberum quiae dolecust imagni iditis secearum este plabore hendell ignimus estion re omnimin conserc illabor sumquis</div>
  <div class="h3" style="left:21px;top:46px">4.4.1 &nbsp;&nbsp; Chronicle of Programs</div>
  <svg class="abs" style="left:14px;top:51px" width="45" height="36" viewBox="0 0 45 36">
    <rect x=".2" y=".2" width="44.6" height="35.6" fill="#fff" stroke="#e3e3e3" stroke-width=".3"/>
    <text x="22.5" y="3.5" font-size="1.8" fill="#777" text-anchor="middle" font-family="Source Sans 3,sans-serif">Sales</text>
    <g transform="translate(22.5,18)">
      <path d="M0,0 L0,-12 A12,12 0 1,1 -7.7,9.2 Z" fill="#140f5e"/>
      <path d="M0,0 L-7.7,9.2 A12,12 0 0,1 -11.4,-3.7 Z" fill="var(--violet)"/>
      <path d="M0,0 L-11.4,-3.7 A12,12 0 0,1 -6.7,-10 Z" fill="#6a5cf0"/>
      <path d="M0,0 L-6.7,-10 A12,12 0 0,1 0,-12 Z" fill="#3a34a8"/>
    </g>
    <g font-size=".9" fill="#777" font-family="Source Sans 3,sans-serif">
      <circle cx="9" cy="33" r=".4" fill="#140f5e"/><text x="9.8" y="33.3">1st Qtr</text>
      <circle cx="16" cy="33" r=".4" fill="var(--violet)"/><text x="16.8" y="33.3">2nd Qtr</text>
      <circle cx="23" cy="33" r=".4" fill="#6a5cf0"/><text x="23.8" y="33.3">3rd Qtr</text>
      <circle cx="30" cy="33" r=".4" fill="#3a34a8"/><text x="30.8" y="33.3">4th Qtr</text>
    </g>
  </svg>
  <div class="cap" style="left:14px;top:89px">Figure 2</div>
  <div class="txt" style="left:63px;top:51px;width:44px;height:49px">nimilig endeles tisque pertiat et faceptiunt quas molorecatem nobis dentem qui blaut quo qui bea voluptatur, iuscid moluptatem. Xerore modi con re con rem ipiditibus, net electot aquisci alitiberum quiae dolecust molorecatem nobis dentem qui blaut quo qui bea voluptatur, iuscid moluptatem. Xerore modi con re con rem ipiditibus, net electot aquisci alitiberum quiae dolecust</div>
  <div class="txt" style="left:14px;top:95px;width:45px;height:45px">molorecatem nobis dentem qui blaut quo qui bea voluptatur, iuscid moluptatem. Xerore modi con re con rem ipiditibus, net electot aquisci alitiberum quiae dolecust dolorio bea lum quis a volores incipit assimag nimilig endeles tisque pertiat et faceptiunt quas molorecatem nobis dentem qui blaut quo qui bea voluptatur, iuscid moluptatem. Xerore modi con re con rem ipiditibus, net electot aquisci alitiberum quiae dolecust imagni iditis secearum este</div>
  <div class="txt" style="left:63px;top:102px;width:44px;height:38px">plabore hendell ignimus estion re omnimin conserc illabor sumquis dolorio bea lum quis a volores incipit assimag nimilig endeles tisque pertiat et faceptiunt quas molorecatem nobis dentem qui blaut quo qui bea voluptatur, iuscid moluptatem. Xerore modi con re con rem ipiditibus, net electot aquisci alitiberum quiae dolecust imagni iditis secearum este plabore hendell ignimus estion re omnimin conserc illabor sumquis</div>
  <div class="ftr-logo">VGL</div><div class="ftr-tab"></div>
</section>

<!-- Short closing page -->
<section class="page" style="left:264px;top:958px">
  <div class="hdr-bar"></div>
  <div class="hdr-note">Confidential and Proprietary - For Veltrix Global<br>International Internal Use Only.</div>
  <div class="txt" style="left:15px;top:15px;width:45px;height:15px">ipiditibus, net electot aquisci alitiberum quiae dolecust imagni iditis secearum este plabore hendell ignimus estion re omnimin conserc illabor sumquis</div>
  <div class="ftr-logo">VGL</div><div class="ftr-tab"></div>
</section>

</body>
</html>
```